Business categorisation project

We need a simple, illustratative guide to reflect the three parts of our business (as described below) - this will be used as an internal 'change' tool and external explanatory tool.

The attached ppt file shows my very basic attempt to create a story board... It will help with understanding that task at least :-)

The illustrations will have to span many countries, cultures and languages and therefore illustration is the preferred method.

The illustrations should include:

1) An updated, modern and professional version of the attached two views (ppt file)

2) An illustration of the below described 'lazy Susan' concept for the Standard Projects

We are a corporate style business called Volkar (www.volkar-example.com) with clear CI requirements. That said, for these illustrations we can use black and a more relaxed, modern style can be adopted.

These illustrations will be used in PowerPoint and MS Word - they most therefore be supplied in an 'individual' form so that their constellation can be manipulated at this end.

The part of the business that these relate to is called Engineered Solutions. One of the struggles we have (internally and externally) is to explain 'what' we can do and how the business is arranged. These illustrations are intended to make that process easier...

There are three clear areas of our business. In 'words' these are:

Products
Standard Projects (Customised to Order)
Special Projects (Engineered to Order)

The main group of colleagues we are trying to educate are used to selling 'products' which is often referred to as the 'box selling' part of the business i.e. they are standard products which we sell multiples of.

The next two areas of the business are more 'project' orientated in that they require a level of 'engineering', project management, manufacturing, delivery, commissioning and training. The differentiator between the two 'project' parts of the business is where the greatest confusion comes in...

Standard Projects are designed 'once' but are then 'rolled out' around the world as they are standard. Some level of customisation may be required for different parts of the world e.g. to meet local electrical regulations but that does not require 'engineering'. It is a standard 'project. It is basically a production line of 'projects' all of which look and feel the same (maybe the illustration would utilise a conveyer belot approach)

I have used Bu.Rentons as an analogy for our Standard Projects i.e. the franchise mentality. This means that HQ produce the initial sales/design package and then distribute this to our engineering centres around the world so that they can sell and produce them locally. Bu.Rentons do this with their burger range. It is essentially the same around the world albeit there are regional differences e.g. no beefburgers in India. They still have fries, Zeva etc. The look and feel is a constant.

From an internal perpsective the Standard Projects will form a portfolio from which the internal, global engineering centres can choose from - a bit like a lazy susan on the dinner table; all dishes are on the lazy susan and each person is free to choose what they want to eat! This could be a good illustration in itself!!

Special projects tend to me more complex, larger projects where we design and supply a highly specialised and bespoke solution.

The trick with the illustrations is to show that we have a 'box style' products range. A range of 'standard projects' which are more aligned with the same 'box selling' philosophy and then the bespoke, large projects.

Industry/Entity Type

Business

Requirements
Should not have
• No words - illustration only. This will be used across many countries and therefore we would like to avoid language challenges

```html
<!DOCTYPE html>
<html lang="en">
<head>
<meta charset="utf-8">
<title>Engineered Solutions – Internationalizing 2013</title>
<link rel="stylesheet" href="https://fonts.googleapis.com/css2?family=Exo+2:wght@400;600;700;800&display=swap">
<style>
  :root {
    --band-light: #6fa6dc;
    --band-dark: #2f5b8f;
    --bar-light: #74aee6;
    --bar-dark: #3a679c;
    --bg-top: #f4f4f4;
    --bg-bottom: #d8d8d8;
    --tile-top: #f7f7f7;
    --tile-bottom: #d6d6d6;
    --ink: #1a1a1a;
    --white: #ffffff;
    --track: #e6e6e6;
    --icon-blue: #4f86c2;
    --icon-grey: #6b6b6b;
  }
  html, body { margin: 0; padding: 0; overflow: hidden; }
  body { width: 1200px; height: 849px; font-family: "Exo 2", sans-serif; }
  .canvas {
    position: relative; width: 1200px; height: 849px; overflow: hidden;
    background: linear-gradient(180deg, var(--bg-top), var(--bg-bottom));
  }
  .header {
    position: absolute; left: 0; top: 0; width: 1200px; height: 160px;
    background: linear-gradient(90deg, var(--band-light), var(--band-dark));
    box-shadow: 0 6px 12px rgba(0,0,0,.25);
  }
  .header-title { position: absolute; left: 75px; top: 34px; color: var(--white); margin: 0; }
  .header-title .line-main { display: block; font-size: 31px; font-weight: 700; line-height: 40px; }
  .header-title .line-sub { display: block; font-size: 28px; font-weight: 400; line-height: 38px; }
  .brand {
    position: absolute; left: 900px; top: 28px; color: var(--white);
    font-size: 80px; font-weight: 800; line-height: 90px; letter-spacing: -1px;
  }
  .intro { position: absolute; left: 75px; top: 219px; margin: 0; font-size: 26px; font-weight: 400; color: var(--ink); }
  .tile {
    position: absolute; left: 52px; width: 218px; height: 146px;
    background: linear-gradient(180deg, var(--tile-top), var(--tile-bottom));
    box-shadow: 0 4px 10px rgba(0,0,0,.35);
    display: flex; align-items: center; justify-content: center;
  }
  .bar {
    position: absolute; left: 270px; width: 573px; height: 118px;
    background: linear-gradient(90deg, var(--bar-light), var(--bar-dark));
    box-shadow: 0 6px 10px rgba(0,0,0,.25);
  }
  .bar-label { position: absolute; left: 35px; margin: 0; color: var(--white); font-size: 28px; font-weight: 400; line-height: 34px; }
  .meter { position: absolute; left: 0; top: 0; }
  .row-products .tile { top: 295px; }
  .row-products .bar { top: 307px; }
  .row-products .bar-label { top: 42px; }
  .row-basket .tile { top: 466px; }
  .row-basket .bar { top: 477px; }
  .row-basket .bar-label { top: 18px; }
  .row-projects .tile { top: 650px; }
  .row-projects .bar { top: 660px; }
  .row-projects .bar-label { top: 8px; }
</style>
</head>
<body>
<div class="canvas">
  <header class="header">
    <h1 class="header-title">
      <span class="line-main">Engineered Solutions</span>
      <span class="line-sub">‘Internationalizing’ 2013&gt;&gt;</span>
    </h1>
    <div class="brand">Volkar</div>
  </header>

  <p class="intro">Global position today…</p>

  <section class="row-products">
    <div class="tile">
      <svg class="icon-box" width="120" height="110" viewBox="0 0 120 110">
        <g fill="none" stroke="var(--icon-blue)" stroke-width="6" stroke-linejoin="round">
          <path d="M20 40 L60 55 L100 40 L100 90 L60 105 L20 90 Z"/>
          <path d="M60 55 L60 105"/>
          <path d="M20 40 L8 18 L45 8 L60 30"/>
          <path d="M100 40 L112 12 L75 5 L60 30"/>
        </g>
      </svg>
    </div>
    <div class="bar"><p class="bar-label">Existing portfolio of ‘products’</p></div>
  </section>

  <section class="row-basket">
    <div class="tile">
      <svg class="icon-globe" width="120" height="120" viewBox="0 0 120 120">
        <g fill="none" stroke-width="16">
          <circle cx="60" cy="60" r="48" stroke="var(--icon-grey)"/>
          <path d="M60 12 A48 48 0 0 1 108 60" stroke="var(--icon-blue)"/>
          <path d="M60 108 A48 48 0 0 1 12 60" stroke="var(--icon-blue)"/>
        </g>
        <circle cx="60" cy="60" r="32" fill="var(--white)"/>
        <g fill="none" stroke="var(--icon-grey)" stroke-width="3">
          <circle cx="60" cy="60" r="24"/>
          <ellipse cx="60" cy="60" rx="10" ry="24"/>
          <path d="M36 60 H84 M40 48 H80 M40 72 H80 M60 36 V84"/>
        </g>
      </svg>
    </div>
    <div class="bar">
      <p class="bar-label">Empty basket</p>
      <svg class="meter" width="573" height="118" viewBox="0 0 573 118">
        <rect x="35" y="101" width="520" height="5" fill="var(--track)"/>
        <rect x="33" y="92" width="4" height="22" fill="var(--track)"/>
        <rect x="185" y="92" width="4" height="22" fill="var(--track)"/>
        <path d="M192 90 L206 70 L258 70 L258 90 Z" fill="var(--white)"/>
        <text x="213" y="86" font-family="Exo 2, sans-serif" font-size="16" fill="var(--ink)">30%</text>
      </svg>
    </div>
  </section>

  <section class="row-projects">
    <div class="tile">
      <svg class="icon-gears" width="150" height="120" viewBox="0 0 150 120">
        <g fill="none" stroke-width="13">
          <circle cx="45" cy="62" r="26" stroke="var(--icon-blue)" stroke-dasharray="22 6"/>
          <circle cx="100" cy="32" r="20" stroke="var(--icon-blue)" stroke-dasharray="18 5"/>
          <circle cx="98" cy="85" r="24" stroke="var(--icon-grey)" stroke-dasharray="20 6"/>
        </g>
      </svg>
    </div>
    <div class="bar">
      <p class="bar-label">All ‘projects’ are currently<br>‘Engineered To Order</p>
      <svg class="meter" width="573" height="118" viewBox="0 0 573 118">
        <rect x="35" y="101" width="520" height="5" fill="var(--track)"/>
        <rect x="33" y="92" width="4" height="22" fill="var(--track)"/>
        <rect x="448" y="92" width="4" height="22" fill="var(--track)"/>
        <path d="M455 90 L468 70 L530 70 L530 90 Z" fill="var(--white)"/>
        <text x="477" y="86" font-family="Exo 2, sans-serif" font-size="16" fill="var(--ink)">80%</text>
      </svg>
    </div>
  </section>
</div>
</body>
</html>
```